Foldable Wireless Headphone Packaging Design

We would like a window box style packaging design for our Foldable Wireless Headphone.

We want to use the packaging for 4-5 of our Wireless headphone series (enclosed picture of the headphones for reference) and hence we would not like to put any product pictures on the packaging.
Material: E-Flute Paper box
Type: Window Box style
Design features we prefer: Colorful, creative, trendy, High tech.
Requirement: AI file is preferred
Size of Packaging: 170 (L) x 120 (W) x 200 (H) mm

Enclosed are a detailed description along with competitor designs for your reference.

Any further questions, please feel free to ask.

Target Market(s)

25-35 year olds

Industry/Entity Type

Electronics

Colors

Designer to choose colors to be used in the design.

Requirements
Must have
• Trendy Design

```html
<!DOCTYPE html>
<html lang="en">
<head>
<meta charset="utf-8">
<title>Foldable Headphone Packaging – Front Panel</title>
<link href="https://fonts.googleapis.com/css2?family=Oswald:wght@300;500;600&family=Arimo:wght@400&display=swap" rel="stylesheet">
<style>
  :root {
    --page: #ffffff;
    --panel-black: #080b0a;
    --accent-orange: #ee8f1f;
    --window-grey: #d8d7d3;
    --window-shade: #bdbcb8;
    --text-white: #f2f2f2;
  }
  * { margin: 0; padding: 0; box-sizing: border-box; }
  html, body {
    width: 1200px; height: 1200px; overflow: hidden;
    background: var(--page);
  }
  .box-front {
    position: absolute; left: 240px; top: 176px;
    width: 720px; height: 848px;
    display: flex;
  }
  .brand-panel {
    position: relative;
    width: 419px; height: 100%;
    background: var(--panel-black);
    overflow: hidden;
  }
  .corner-flash {
    position: absolute; left: 0; top: 0;
  }
  .brand-mark {
    position: absolute; left: 34px; top: 30px;
    display: flex; flex-direction: column; align-items: center;
  }
  .brand-mark .square {
    width: 26px; height: 26px;
    background: var(--panel-black);
  }
  .brand-mark .name {
    margin-top: 8px;
    font-family: "Oswald", sans-serif; font-weight: 500;
    font-size: 24px; line-height: 1;
    color: var(--panel-black);
  }
  .headline {
    position: absolute; left: 0; top: 228px; width: 100%;
    text-align: center;
    font-family: "Oswald", sans-serif;
    color: var(--text-white);
  }
  .headline .line {
    display: block;
    font-weight: 300; font-size: 46px; line-height: 1;
  }
  .headline .line.top { letter-spacing: 4px; }
  .headline .line.bottom { letter-spacing: 1px; }
  .headline .tag {
    display: inline-block;
    margin: 12px 0 12px;
    width: 202px; height: 42px;
    border: 3px solid var(--accent-orange);
    color: var(--accent-orange);
    font-weight: 600; font-size: 29px; line-height: 36px;
    letter-spacing: 7px; padding-left: 7px;
  }
  .features {
    position: absolute; left: 0; top: 652px; width: 100%;
    list-style: none; text-align: center;
    font-family: "Arimo", sans-serif; font-size: 16px;
  }
  .features li { height: 37px; line-height: 28px; color: var(--text-white); }
  .features li.alt { color: var(--accent-orange); }
  .product-window {
    width: 301px; height: 100%;
    background: radial-gradient(ellipse at 35% 55%, var(--window-shade) 0%, var(--window-grey) 60%);
  }
</style>
</head>
<body>
  <div class="box-front">
    <section class="brand-panel">
      <svg class="corner-flash" width="304" height="237" viewBox="0 0 304 237">
        <polygon points="0,0 304,0 0,237" fill="var(--accent-orange)"/>
      </svg>
      <div class="brand-mark">
        <span class="square"></span>
        <span class="name">Sonvia</span>
      </div>
      <h1 class="headline">
        <span class="line top">FOLDABLE</span>
        <span class="tag">WIRELESS</span>
        <span class="line bottom">HEADPHONE</span>
      </h1>
      <ul class="features">
        <li>Wireless V5</li>
        <li class="alt">Foldable and Portable</li>
        <li>Exceptional Sound Quality</li>
        <li class="alt">Dual Mode wireless or wired connectivity</li>
        <li>Adjustable headband</li>
      </ul>
    </section>
    <div class="product-window" role="img" aria-label="Window showing the folded black headphones with a red accent ring on the ear cup"></div>
  </div>
</body>
</html>
```